Supplement Rebranding Bottle Design

READ WORD DOCUMENT ATTACHED.
We want to rebrand our current health supplements (see below). We do want it to be modern, vibrant and appealing. Very upscale and elegant as it targets primarily women.
Bottle size: see pictures for bottle size, along with sample bottles that we like; we’re open to any bottle similar to the ones attached.
Current bottles: So ideally, we’d keep the core color on each bottle with a new branding/bottle design. But we're open to your suggestion.

Target Market(s)

mostly women but shouldn't be overly feminine

Requirements
Must have
• see bottle sizes attached

```html
<!DOCTYPE html>
<html lang="en">
<head>
<meta charset="utf-8">
<title>Hormone Align – Supplement Label</title>
<link rel="stylesheet" href="https://fonts.googleapis.com/css2?family=Jost:wght@300;400;600;700&family=Roboto+Condensed:wght@700&display=swap">
<style>
  :root {
    --page-bg: #eeeeee;
    --label-bg: #ffffff;
    --ink: #2a2a2a;
    --leaf-green: #2f8a16;
    --deep-green: #216f0f;
    --band-dark: #2b2b2b;
    --white: #ffffff;
  }
  * { margin: 0; padding: 0; box-sizing: border-box; }
  html, body {
    width: 1200px; height: 1200px; overflow: hidden;
    background: var(--page-bg);
  }
  .label {
    position: absolute; left: 220px; top: 125px;
    width: 760px; height: 950px;
    background: var(--label-bg);
    box-shadow: 0 2px 14px rgba(0,0,0,0.08);
    font-family: "Jost", sans-serif;
    color: var(--ink);
  }
  .brand {
    position: absolute; left: 0; right: 0; top: 150px;
    display: flex; justify-content: center; align-items: center; gap: 12px;
  }
  .brand-dot {
    width: 14px; height: 14px; border-radius: 50%;
    background: var(--ink);
  }
  .brand-name {
    font-weight: 400; font-size: 30px; letter-spacing: 1px;
  }
  .product-name {
    position: absolute; left: 0; right: 0; top: 288px;
    text-align: center; line-height: 1;
  }
  .product-name .line-bold {
    display: block; font-weight: 700; font-size: 118px; letter-spacing: 2px;
  }
  .product-name .line-light {
    display: block; font-weight: 400; font-size: 118px; margin-top: 2px;
  }
  .tagline {
    position: absolute; left: 0; right: 0; top: 556px;
    text-align: center; font-weight: 600; font-size: 23px; letter-spacing: 0.5px;
  }
  .tagline sup { font-size: 15px; }
  .molecule {
    position: absolute; border-radius: 40%;
    background: radial-gradient(circle, rgba(47,138,22,0.55) 0%, rgba(47,138,22,0.15) 70%, rgba(47,138,22,0) 100%);
  }
  .molecule-left { left: 50px; top: 572px; width: 166px; height: 249px; }
  .molecule-right { left: 588px; top: 644px; width: 156px; height: 177px; }
  .count-arch {
    position: absolute; left: 294px; top: 622px;
    width: 176px; height: 230px;
    background: var(--deep-green);
    border-radius: 88px 88px 0 0;
    color: var(--white); text-align: center;
  }
  .count-number {
    display: block; margin-top: 52px;
    font-weight: 400; font-size: 82px; line-height: 1;
  }
  .count-unit {
    display: block; margin-top: 10px;
    font-weight: 600; font-size: 15px; letter-spacing: 1.5px; line-height: 1.2;
  }
  .format-band {
    position: absolute; left: 159px; top: 838px;
    width: 438px; height: 58px;
  }
  .format-band svg { position: absolute; inset: 0; }
  .format-band span {
    position: relative; display: block; text-align: center;
    font-family: "Roboto Condensed", sans-serif; font-weight: 700;
    font-size: 38px; line-height: 58px; color: var(--white);
  }
</style>
</head>
<body>
  <main class="label">
    <div class="brand">
      <span class="brand-dot"></span>
      <span class="brand-name">AVA LINDEN</span>
    </div>

    <h1 class="product-name">
      <span class="line-bold">HORMONE</span>
      <span class="line-light">ALIGN</span>
    </h1>

    <p class="tagline">Supports Healthy Hormone Levels<sup>*</sup></p>

    <div class="molecule molecule-left" role="img" aria-label="Green molecule graphic"></div>
    <div class="molecule molecule-right" role="img" aria-label="Green molecule graphic"></div>

    <div class="count-arch">
      <span class="count-number">60</span>
      <span class="count-unit">VEGETABLE<br>CAPSULES</span>
    </div>

    <div class="format-band">
      <svg width="438" height="58" viewBox="0 0 438 58" aria-hidden="true">
        <path d="M28 0 H410 Q418 0 421 6 L436 46 Q440 58 426 58 H12 Q-2 58 2 46 L17 6 Q20 0 28 0 Z" fill="var(--band-dark)"/>
      </svg>
      <span>DIETARY SUPPLEMENT</span>
    </div>
  </main>
</body>
</html>
```